Real estate broker business card

Want a modern celan but effective business card for my residential and commercial real estate business. I want the back of the card to advertise my services and to capture business. I have attached the back of my current business card fore ideas
Updates

Target Market(s)

home buyers and seller. commercial buyers and sellers

Industry/Entity Type

Real Estate

Contact Information for Business Card

must have my contact information and my photo

Requirements
Must have
• Lorna Vettridge
• Owner & Qualifying Broker
• Brockhill Real Estate Services
• 555.218.7094
• lorna@brockhillhomes.example
• www.brockhillhomes.example
Nice to have
• metallic
• Business capture text: " Don't buy or lease property without someone looking out for your best interests. I will represent you on your home or investment purchase for FREE!"
• "Home owners, call today to receive a FREE market analysis for your homes value!

```html
<!DOCTYPE html>
<html lang="en">
<head>
<meta charset="utf-8">
<title>Brockhill Real Estate Services – Business Card</title>
<link rel="stylesheet" href="https://fonts.googleapis.com/css2?family=Marcellus&family=Open+Sans:wght@400;600&display=swap">
<style>
  :root {
    --page-bg: #d9d9d9;
    --card-black: #050505;
    --card-charcoal: #1c1c1c;
    --card-white: #ffffff;
    --teal: #1d7f8c;
    --teal-icon: #2a97a6;
    --silver-dark: #5a5a5a;
    --silver-mid: #c9c9c9;
    --silver-light: #f4f4f4;
    --ink: #111111;
    --contact-grey: #b5b5b5;
  }
  * { box-sizing: border-box; margin: 0; padding: 0; }
  html, body { width: 1200px; height: 895px; overflow: hidden; }
  body { background: var(--page-bg); position: relative; }

  .card {
    position: absolute;
    left: 323px;
    width: 553px;
    height: 313px;
    border-radius: 14px;
    overflow: hidden;
  }

  /* Front */
  .card--front {
    top: 117px;
    background: linear-gradient(135deg, var(--card-charcoal) 0%, var(--card-black) 55%);
  }
  .front__brand {
    position: absolute;
    left: 32px;
    top: 50px;
    width: 240px;
    font-family: "Marcellus", serif;
    font-size: 17px;
    line-height: 1.25;
    letter-spacing: 1.5px;
    color: var(--teal);
    text-transform: uppercase;
  }
  .front__band {
    position: absolute;
    left: 0;
    top: 130px;
    width: 330px;
    height: 58px;
    background: linear-gradient(90deg, var(--silver-dark) 0%, var(--silver-mid) 25%, var(--silver-light) 55%, var(--silver-mid) 80%, var(--silver-dark) 100%);
  }
  .front__name {
    position: absolute;
    left: 63px;
    top: 8px;
    font-family: "Marcellus", serif;
    font-size: 21px;
    color: var(--ink);
    letter-spacing: 0.5px;
    font-variant: small-caps;
  }
  .front__role {
    position: absolute;
    left: 63px;
    top: 35px;
    font-family: "Open Sans", sans-serif;
    font-weight: 600;
    font-size: 12.5px;
    color: var(--ink);
  }
  .front__contacts {
    position: absolute;
    left: 32px;
    top: 228px;
    list-style: none;
    font-family: "Open Sans", sans-serif;
    font-size: 13px;
    color: var(--contact-grey);
  }
  .front__contacts li {
    display: flex;
    align-items: center;
    height: 18.5px;
  }
  .front__contacts svg {
    width: 14px;
    height: 14px;
    margin-right: 7px;
    fill: var(--teal-icon);
  }
  .front__photo {
    position: absolute;
    right: 0;
    top: 0;
    width: 235px;
    height: 100%;
    background: radial-gradient(ellipse at 55% 45%, #6b4a3a 0%, #3a2a22 40%, #111 75%),
                linear-gradient(180deg, #111 0%, #ddd 100%);
    -webkit-mask-image: linear-gradient(90deg, transparent 0%, #000 25%);
            mask-image: linear-gradient(90deg, transparent 0%, #000 25%);
  }

  /* Back */
  .card--back {
    top: 473px;
    background: var(--card-white);
  }
  .back__mark {
    position: absolute;
    left: 246px;
    top: 70px;
    width: 60px;
    height: 60px;
    background: var(--teal);
  }
  .back__brand {
    position: absolute;
    left: 0;
    right: 0;
    top: 168px;
    text-align: center;
    font-family: "Marcellus", serif;
    color: var(--teal);
    text-transform: uppercase;
  }
  .back__brand-name {
    display: block;
    font-size: 44px;
    line-height: 1;
    letter-spacing: 1px;
  }
  .back__brand-tag {
    display: block;
    margin-top: 8px;
    font-size: 17px;
    letter-spacing: 2.5px;
  }
</style>
</head>
<body>

<section class="card card--front" aria-label="Business card front">
  <p class="front__brand">Brockhill Real Estate Services</p>

  <div class="front__band">
    <h1 class="front__name">Lorna Vettridge</h1>
    <p class="front__role">Owner &amp; Qualifying Broker</p>
  </div>

  <ul class="front__contacts">
    <li>
      <svg viewBox="0 0 16 16" aria-hidden="true"><path d="M2 5c0-2 3-3 6-3s6 1 6 3v1h-3V5H5v1H2z"/><path d="M4 7h8l2 6H2z"/></svg>
      555.218.7094
    </li>
    <li>
      <svg viewBox="0 0 16 16" aria-hidden="true"><path d="M1 3h14v10H1z"/><path d="M1 3l7 6 7-6" fill="none" stroke="#050505" stroke-width="1.4"/></svg>
      lorna@brockhillhomes.example
    </li>
    <li>
      <svg viewBox="0 0 16 16" aria-hidden="true"><circle cx="8" cy="8" r="7"/><path d="M1 8h14M8 1c-3 4-3 10 0 14M8 1c3 4 3 10 0 14" fill="none" stroke="#050505" stroke-width="1"/></svg>
      www.brockhillhomes.example
    </li>
  </ul>

  <div class="front__photo" role="img" aria-label="Portrait photo of the broker, Lorna Vettridge"></div>
</section>

<section class="card card--back" aria-label="Business card back">
  <div class="back__mark" aria-hidden="true"></div>
  <p class="back__brand">
    <span class="back__brand-name">Brockhill</span>
    <span class="back__brand-tag">Real Estate Services</span>
  </p>
</section>

</body>
</html>
```